Business Card for Web Design consulting firm

Business card designs for Web Design consulting firm

Target Market(s)

English speaking adults ages 30 - 60. Predominantly professional services eg. Doctor, Dentist

Industry/Entity Type

Consulting

Requirements
Must have
• Double sided card

```html
<!DOCTYPE html>
<html lang="en">
<head>
<meta charset="utf-8">
<title>Corvant – business card concepts</title>
<link rel="stylesheet" href="https://fonts.googleapis.com/css2?family=Carlito&family=Open+Sans:wght@400;600;700&display=swap">
<style>
  :root {
    --orange: #f39a1f;
    --orange-soft: #f6b24f;
    --orange-pale: #fbe3c2;
    --charcoal: #4a4a4a;
    --charcoal-dark: #3f3f3f;
    --paper: #ffffff;
    --mist: #f1f1f1;
    --edge: #cfcfcf;
    --ink: #333333;
    --dash: #b9c98a;
  }
  * { box-sizing: border-box; margin: 0; padding: 0; }
  html, body { width: 1200px; height: 885px; overflow: hidden; background: var(--paper); }
  body { position: relative; font-family: "Open Sans", Arial, sans-serif; color: var(--ink); }

  .board-label {
    position: absolute; left: 20px;
    font-family: "Carlito", "Open Sans", sans-serif;
    font-size: 30px; font-weight: 400; color: #222;
  }
  .board-label--one { top: 18px; }
  .board-label--two { top: 440px; }

  .card {
    position: absolute; width: 560px;
    background: var(--paper);
    border: 1px solid var(--edge);
    box-shadow: 1px 2px 4px rgba(0,0,0,.12);
    overflow: hidden;
  }
  .card--d1-front { left: 20px; top: 70px; height: 340px; }
  .card--d1-back  { left: 620px; top: 70px; height: 340px; }
  .card--d2-front { left: 20px; top: 490px; height: 375px; }
  .card--d2-back  { left: 620px; top: 490px; height: 375px; }

  .layer { position: absolute; }

  /* brand block standing in for the mark */
  .brand {
    position: absolute;
    display: flex; align-items: center; justify-content: center; gap: 8px;
    background: var(--mist);
  }
  .brand__dot { width: 14px; height: 14px; background: var(--orange); }
  .brand__name {
    font-weight: 600; font-size: 24px; letter-spacing: 1px;
    color: var(--charcoal);
  }

  .tagline { position: absolute; color: var(--paper); font-size: 11px; white-space: nowrap; }

  /* Design 1 front */
  .d1-front__texture {
    inset: 0;
    background: linear-gradient(135deg, #fdf0dc 0%, var(--orange-pale) 45%, #f9d7a6 100%);
  }
  .d1-front__panel {
    left: 67px; top: 0; width: 168px; height: 245px;
    background: var(--orange); color: var(--paper);
    text-align: center; padding-top: 60px;
  }
  .person-name { font-weight: 700; font-size: 13px; }
  .person-role { font-size: 12px; }
  .d1-front__rule { left: 262px; top: 0; height: 322px; border-left: 1px dashed var(--dash); }
  .d1-front__brand { left: 95px; top: 232px; width: 165px; height: 90px; }
  .d1-front__band { left: 0; right: 0; bottom: 0; height: 18px; background: var(--charcoal); }
  .d1-front__band .tagline { left: 112px; top: 1px; }

  /* Design 1 back */
  .d1-back__texture { inset: 0; background: linear-gradient(90deg, #f4f4f4, #fafafa 50%, #f2f2f2); }
  .d1-back__panel {
    left: 263px; top: 0; width: 150px; height: 218px;
    background: var(--charcoal); color: var(--paper);
    border-left: 1px dashed var(--dash);
    padding: 38px 0 0 10px; font-size: 10.5px; line-height: 26px; white-space: nowrap;
  }
  .d1-back__brand { left: 263px; top: 218px; width: 150px; height: 66px; border: 1px dashed #bbb; }
  .d1-back__brand .brand__name { font-size: 19px; }
  .d1-back__band { left: 0; right: 0; top: 292px; height: 16px; background: var(--orange); }
  .d1-back__band .tagline { left: 282px; top: 0; font-size: 10px; }

  /* Design 2 shared */
  .fieldrow { position: absolute; display: flex; align-items: center; gap: 6px; font-size: 11px; white-space: nowrap; }
  .fieldrow__tab { width: 6px; height: 16px; background: var(--paper); }
  .fieldrow__label { font-weight: 700; color: var(--paper); font-size: 12px; }
  .fieldrow__value { background: var(--paper); color: var(--ink); height: 16px; line-height: 16px; padding: 0 4px; }
  .ghost-name {
    position: absolute; font-weight: 700; font-size: 96px; letter-spacing: 4px;
    white-space: nowrap; pointer-events: none;
  }

  /* Design 2 front */
  .d2-front__heading { right: 12px; top: 10px; text-align: right; color: var(--ink); }
  .d2-front__block { left: 246px; top: 52px; width: 314px; height: 293px; background: var(--orange); overflow: hidden; }
  .d2-front__block .ghost-name { left: 10px; top: 170px; color: var(--orange-soft); }
  .d2-front__block .fieldrow { left: 6px; top: 128px; }
  .d2-front__block .fieldrow__value { width: 86px; text-align: center; }
  .d2-front__band { left: 0; right: 0; top: 345px; height: 22px; background: var(--charcoal); }
  .d2-front__band .tagline { left: 262px; top: 3px; font-size: 10px; letter-spacing: 5px; }
  .d2-front__brand { left: 25px; top: 252px; width: 160px; height: 85px; }
  .d2-front__link { left: 0; top: 0; }

  /* Design 2 back */
  .d2-back__heading { left: 8px; top: 6px; font-size: 11px; }
  .d2-back__heading strong { font-size: 12px; display: block; }
  .d2-back__block { left: 4px; top: 66px; width: 310px; height: 246px; background: var(--charcoal); overflow: hidden; }
  .d2-back__block .ghost-name { left: 8px; top: 130px; color: var(--charcoal-dark); }
  .d2-back__fields { left: 4px; top: 178px; gap: 4px; font-size: 10.5px; }
  .d2-back__fields .fieldrow__label { font-size: 11.5px; }
  .d2-back__band { left: 314px; right: 0; top: 300px; height: 10px; background: var(--orange); }
  .d2-back__tagline { left: 10px; top: 316px; color: var(--orange); font-size: 10px; letter-spacing: 5px; white-space: nowrap; }
  .d2-back__brand { right: 8px; top: 212px; width: 155px; height: 80px; }
  .d2-back__link { left: 0; top: 0; }
</style>
</head>
<body>

<h2 class="board-label board-label--one">Design 1</h2>

<section class="card card--d1-front" aria-label="Design 1 front">
  <div class="layer d1-front__texture" role="img" aria-label="Soft orange binary-digit background texture"></div>
  <div class="layer d1-front__panel">
    <p class="person-name">corvant</p>
    <p class="person-role">head-operations</p>
  </div>
  <div class="layer d1-front__rule"></div>
  <div class="brand d1-front__brand"><span class="brand__dot"></span><span class="brand__name">CORVANT</span></div>
  <div class="layer d1-front__band"><span class="tagline">web design consulting firm</span></div>
</section>

<section class="card card--d1-back" aria-label="Design 1 back">
  <div class="layer d1-back__texture" role="img" aria-label="Faint grey web-address text texture"></div>
  <div class="layer d1-back__panel">
    <p>home town://</p>
    <p>corvant@101010.australia</p>
    <p>Ph:// 101010 &nbsp;fax:// 101010</p>
    <p>email: hello@corvant.com</p>
    <p>website: www.corvant.com</p>
  </div>
  <div class="brand d1-back__brand"><span class="brand__dot"></span><span class="brand__name">CORVANT</span></div>
  <div class="layer d1-back__band"><span class="tagline">web design consulting firm</span></div>
</section>

<h2 class="board-label board-label--two">Design 2</h2>

<section class="card card--d2-front" aria-label="Design 2 front">
  <div class="layer d2-front__heading">
    <p class="person-name">corvant</p>
    <p class="person-role">head-operations</p>
  </div>
  <div class="layer d2-front__block">
    <span class="ghost-name" aria-hidden="true">CORVANT</span>
    <div class="fieldrow">
      <span class="fieldrow__tab"></span>
      <span class="fieldrow__label">phone</span>
      <span class="fieldrow__value">101010</span>
      <span class="fieldrow__label">fax</span>
      <span class="fieldrow__value">101010</span>
    </div>
  </div>
  <div class="layer d2-front__band"><span class="tagline">web design consulting firm</span></div>
  <svg class="layer d2-front__link" width="560" height="375" aria-hidden="true">
    <line x1="182" y1="322" x2="262" y2="352" stroke="var(--orange)" stroke-width="5"/>
  </svg>
  <div class="brand d2-front__brand"><span class="brand__dot"></span><span class="brand__name">CORVANT</span></div>
</section>

<section class="card card--d2-back" aria-label="Design 2 back">
  <div class="layer d2-back__heading">
    <strong>home town</strong>
    corvant@101010.australia
  </div>
  <div class="layer d2-back__block">
    <span class="ghost-name" aria-hidden="true">CORVANT</span>
  </div>
  <div class="fieldrow d2-back__fields">
    <span class="fieldrow__tab"></span>
    <span class="fieldrow__label">website</span>
    <span class="fieldrow__value">www.corvant.com</span>
    <span class="fieldrow__label">email</span>
    <span class="fieldrow__value">hello@corvant.com</span>
  </div>
  <div class="layer d2-back__band"></div>
  <p class="layer d2-back__tagline">web design consulting firm</p>
  <svg class="layer d2-back__link" width="560" height="375" aria-hidden="true">
    <line x1="312" y1="300" x2="400" y2="272" stroke="var(--charcoal)" stroke-width="5"/>
  </svg>
  <div class="brand d2-back__brand"><span class="brand__dot"></span><span class="brand__name">CORVANT</span></div>
</section>

</body>
</html>
```